Bright Oak Fitness Facility Business Cards

Business Card Design that incorporates the logo and tagline

Target Market(s)

Fitness, People Who Exercise

Contact Information for Business Card

2817 Mossgrove Bend Road
Tavares, Florida 32190
Phone: 352-555-Jump (5867)
www.brightoakfitness.example
info@brightoakfitness.example

Requirements
Must have
• Logo, Address, Website, email and tagline "More Than A Gym". Colors should be red/black/grey/white

```html
<!DOCTYPE html>
<html lang="en">
<head>
<meta charset="utf-8">
<title>Bright Oak Fitness – Business Cards</title>
<link href="https://fonts.googleapis.com/css2?family=Source+Sans+3:ital,wght@0,400;0,600;0,700;1,400&display=swap" rel="stylesheet">
<style>
  :root {
    --stage: #e9e9e9;
    --card-dark: #070707;
    --card-light: #ffffff;
    --brand-red: #e8202a;
    --ink: #1e1e1e;
    --ink-soft: #333333;
  }
  html, body {
    margin: 0;
    padding: 0;
    width: 1200px;
    height: 1200px;
    overflow: hidden;
    background: var(--stage);
    font-family: "Source Sans 3", "Myriad Pro", Arial, sans-serif;
  }
  .canvas {
    position: relative;
    width: 1200px;
    height: 1200px;
  }
  .card {
    position: absolute;
    left: 250px;
    width: 700px;
    height: 398px;
    box-shadow: 0 4px 12px rgba(0,0,0,0.25);
  }
  .card--front {
    top: 148px;
    background: var(--card-dark);
  }
  .card--back {
    top: 651px;
    background: var(--card-light);
  }
  .brand {
    position: absolute;
    display: flex;
    align-items: center;
    gap: 12px;
    font-weight: 700;
    letter-spacing: 0.5px;
    white-space: nowrap;
  }
  .brand__mark {
    width: 16px;
    height: 16px;
    background: var(--brand-red);
  }
  .card--front .brand {
    left: 0;
    right: 0;
    top: 178px;
    justify-content: center;
    font-size: 40px;
    color: #ffffff;
  }
  .tagline {
    position: absolute;
    left: 0;
    right: 0;
    top: 318px;
    text-align: center;
    font-style: italic;
    font-size: 18px;
    color: var(--brand-red);
  }
  .card--back .brand {
    right: 46px;
    top: 70px;
    font-size: 28px;
    color: var(--ink);
  }
  .contact {
    position: absolute;
    left: 48px;
    top: 146px;
    color: var(--ink-soft);
    font-size: 18px;
    line-height: 23px;
  }
  .contact__name {
    color: var(--brand-red);
    font-weight: 700;
    font-size: 18px;
    letter-spacing: 0.3px;
  }
  .contact__address {
    margin-top: 28px;
  }
  .contact__lines {
    margin-top: 10px;
  }
  .contact__line {
    display: flex;
    align-items: center;
    gap: 9px;
  }
  .contact__icon {
    width: 15px;
    height: 15px;
    fill: var(--ink);
    flex: none;
  }
</style>
</head>
<body>
<main class="canvas">
  <section class="card card--front">
    <div class="brand"><span class="brand__mark"></span>Bright Oak Fitness</div>
    <p class="tagline">More Than A Gym</p>
  </section>

  <section class="card card--back">
    <div class="brand"><span class="brand__mark"></span>Bright Oak Fitness</div>
    <div class="contact">
      <div class="contact__name">MARK ELLISON</div>
      <div class="contact__role">Managing Director</div>
      <div class="contact__address">
        2817 Mossgrove Bend Road<br>
        Tavares, Florida 32190
      </div>
      <div class="contact__lines">
        <div class="contact__line">
          <svg class="contact__icon" viewBox="0 0 16 16" aria-hidden="true"><path d="M1 6c0-2 3-4 7-4s7 2 7 4v1h-4V5.5c-1-.4-5-.4-6 0V7H1z M4 8h8l2 6H2z"/></svg>
          Phone: 352-555-Jump (5867)
        </div>
        <div class="contact__line">
          <svg class="contact__icon" viewBox="0 0 16 16" aria-hidden="true"><path d="M1 3h14v10H1z M2 4l6 5 6-5v-.5H2z" fill-rule="evenodd"/></svg>
          info@brightoakfitness.example
        </div>
        <div class="contact__line">
          <svg class="contact__icon" viewBox="0 0 16 16" aria-hidden="true"><g fill="none" stroke="#1e1e1e" stroke-width="1.3"><circle cx="8" cy="8" r="6.5"/><ellipse cx="8" cy="8" rx="2.8" ry="6.5"/><path d="M1.5 8h13M2.5 4.8h11M2.5 11.2h11"/></g></svg>
          www.brightoakfitness.example
        </div>
      </div>
    </div>
  </section>
</main>
</body>
</html>
```